Business Card Design for Concierge business

Hi. I would like to have an elegant, smart business card for my concierge business, called Harbor Concierge. The services I provide are mail management, dog walking, cleaning, car, stylist, personal shopper, running errands, property management, event planning. I was thinking to add my picture but I would like to see options without it as well, if possible.

Thank you.

Business Card Details:
*Designers are to solely use contact information for the business card design. This is not to be used to contact the customer*

Name: Tamsin Heller
mail: quaylineerrands@mailvora.net
Phone: 305-482-9167

Target Market(s)

vacation home owners

Industry/Entity Type

Business

Font styles to use
Serif

Colors

Designer to choose colors to be used in the design.

Requirements
Nice to have
• Could use icons that describe the services I provide for example car, house, key, shopping cart, shopping bags, envelope, champagne glasses, phone, dog etc.

```html
<!DOCTYPE html>
<html lang="en">
<head>
<meta charset="utf-8">
<title>Harbor Concierge – Business Cards</title>
<link rel="stylesheet" href="https://fonts.googleapis.com/css2?family=Cinzel:wght@400;600&family=Montserrat:wght@500;600&display=swap">
<style>
  :root {
    --backdrop: #2a2a2a;
    --card: #141414;
    --card-edge: #1d1d1d;
    --gold: #c9a24a;
    --ink-dark: #111111;
    --text-light: #f4f4f4;
  }
  * { box-sizing: border-box; margin: 0; padding: 0; }
  html, body { width: 1200px; height: 1000px; overflow: hidden; }
  body {
    background: var(--backdrop);
    display: flex;
    flex-direction: column;
    align-items: center;
    justify-content: center;
    gap: 60px;
  }
  .card {
    position: relative;
    width: 700px;
    height: 400px;
    background: linear-gradient(160deg, var(--card-edge), var(--card));
    box-shadow: 0 18px 40px rgba(0,0,0,0.55);
    overflow: hidden;
  }
  .wordmark {
    position: absolute;
    left: 0; right: 0;
    text-align: center;
    font-family: "Cinzel", serif;
    font-weight: 400;
    color: var(--text-light);
    font-size: 54px;
    letter-spacing: 1px;
  }
  .card--front .wordmark { top: 105px; }
  .service-icons {
    position: absolute;
    top: 245px;
    left: 0; right: 0;
    display: flex;
    justify-content: center;
    gap: 26px;
  }
  .service-icon {
    width: 46px; height: 46px;
    border-radius: 50%;
    background: var(--gold);
    display: flex; align-items: center; justify-content: center;
  }
  .service-icon svg { width: 26px; height: 26px; }
  .card--back .wordmark { top: 85px; }
  .contact {
    position: absolute;
    top: 220px;
    left: 0; right: 0;
    text-align: center;
    color: var(--text-light);
  }
  .contact__name {
    font-family: "Cinzel", serif;
    font-size: 26px;
    letter-spacing: 1px;
    margin-bottom: 8px;
  }
  .contact__phone {
    font-family: "Montserrat", sans-serif;
    font-weight: 600;
    font-size: 20px;
    display: inline-flex; align-items: center; gap: 8px;
    margin-bottom: 10px;
  }
  .contact__phone-dot {
    width: 16px; height: 16px; border-radius: 50%;
    background: var(--gold);
    display: inline-flex; align-items: center; justify-content: center;
  }
  .contact__email {
    font-family: "Montserrat", sans-serif;
    font-weight: 500;
    font-size: 17px;
  }
</style>
</head>
<body>

<section class="card card--front">
  <div class="wordmark">Harbor Concierge</div>
  <div class="service-icons">
    <div class="service-icon" aria-label="Mail">
      <svg viewBox="0 0 24 24"><path d="M12 2 L4 21 L12 17 L20 21 Z" fill="var(--ink-dark)"/><path d="M12 2 L12 17" stroke="var(--gold)" stroke-width="1"/></svg>
    </div>
    <div class="service-icon" aria-label="Phone">
      <svg viewBox="0 0 24 24"><rect x="6" y="2" width="12" height="20" rx="2" fill="none" stroke="var(--ink-dark)" stroke-width="2"/><circle cx="12" cy="18.5" r="1" fill="var(--ink-dark)"/></svg>
    </div>
    <div class="service-icon" aria-label="Shopping">
      <svg viewBox="0 0 24 24"><path d="M2 4 H5 L8 16 H19 L21 8 H6" fill="none" stroke="var(--ink-dark)" stroke-width="2" stroke-linejoin="round"/><circle cx="9" cy="20" r="1.6" fill="var(--ink-dark)"/><circle cx="17" cy="20" r="1.6" fill="var(--ink-dark)"/></svg>
    </div>
    <div class="service-icon" aria-label="Car">
      <svg viewBox="0 0 24 24"><path d="M3 15 V12 L6 7 H18 L21 12 V15 Z" fill="var(--ink-dark)"/><rect x="7.5" y="8.5" width="9" height="3" fill="var(--gold)"/><circle cx="7" cy="16" r="2.2" fill="var(--ink-dark)"/><circle cx="17" cy="16" r="2.2" fill="var(--ink-dark)"/></svg>
    </div>
    <div class="service-icon" aria-label="Stylist">
      <svg viewBox="0 0 24 24"><circle cx="6" cy="18" r="2.5" fill="none" stroke="var(--ink-dark)" stroke-width="2"/><circle cx="11" cy="20" r="2.5" fill="none" stroke="var(--ink-dark)" stroke-width="2"/><path d="M7.5 16 L20 4 M10 17.5 L15 6" stroke="var(--ink-dark)" stroke-width="2"/></svg>
    </div>
    <div class="service-icon" aria-label="Events">
      <svg viewBox="0 0 24 24"><path d="M5 3 H11 L10 9 A2 2 0 0 1 6 9 Z M8 11 V19 M5.5 20 H10.5" fill="var(--ink-dark)" stroke="var(--ink-dark)" stroke-width="1.5"/><path d="M13 3 H19 L18 9 A2 2 0 0 1 14 9 Z M16 11 V19 M13.5 20 H18.5" fill="var(--ink-dark)" stroke="var(--ink-dark)" stroke-width="1.5"/></svg>
    </div>
  </div>
</section>

<section class="card card--back">
  <div class="wordmark">Harbor Concierge</div>
  <div class="contact">
    <p class="contact__name">Tamsin Heller</p>
    <p class="contact__phone">
      <span class="contact__phone-dot">
        <svg viewBox="0 0 24 24" width="10" height="10"><path d="M6 3 L9 3 L10 8 L8 9.5 A12 12 0 0 0 14.5 16 L16 14 L21 15 L21 18 A3 3 0 0 1 18 21 A15 15 0 0 1 3 6 A3 3 0 0 1 6 3 Z" fill="var(--ink-dark)"/></svg>
      </span>
      305-482-9167
    </p>
    <p class="contact__email">quaylineerrands@mailvora.net</p>
  </div>
</section>

</body>
</html>
```